Peer-to-peer Car Rental Business needs a business card design

We need a business card design for a new company based in Melbourne, Australia called "Wheelnest". We enable car owners to earny money by renting out their car to others in the community/neighbourhood when their not using it.
We would like to see designs that use the colour/s blue and/or orange.
The design should communicate young, modern, fun etc.
The themes to use should be community/neighbourhood, cars, parking, airports, car rental, sharing.

Our current logo is attached.

Target Market(s)

Young adults aged 20-35, travellers, environmentally conscious, cost conscious.

Industry/Entity Type

Business

Requirements
Must have
• Must have fields for persons name, title, mobile number, email company website.

```html
<!DOCTYPE html>
<html lang="en">
<head>
<meta charset="utf-8">
<title>Wheelnest business card</title>
<link rel="stylesheet" href="https://fonts.googleapis.com/css2?family=Arimo:wght@400;700&family=Tinos:wght@700&display=swap">
<style>
  :root {
    --orange: #e07a1c;
    --plum: #5a2f5e;
    --navy: #2a1d6e;
    --logo-blue: #3a4f86;
    --cream: #f6e6b0;
    --yellow: #ffe11a;
    --peach: #f4c193;
    --pale-yellow: #fdf6a8;
    --ink: #1a1a1a;
    --blank: #ffffff;
  }
  * { margin: 0; padding: 0; box-sizing: border-box; }
  html, body { width: 759px; height: 1200px; overflow: hidden; background: var(--blank); }
  .canvas { position: relative; width: 759px; height: 1200px; }

  .card-front {
    position: absolute; left: 0; top: 0; width: 759px; height: 445px;
    background: linear-gradient(90deg, var(--orange) 0%, var(--plum) 45%, var(--navy) 100%);
  }
  .front-logo-band {
    position: absolute; left: 0; top: 46px; width: 577px; height: 97px;
    background: linear-gradient(90deg, #fffbe6 0%, #fbf4d6 70%, rgba(251,244,214,0) 100%);
  }
  .brand-name {
    font-family: "Arimo", Arial, sans-serif; font-weight: 400;
    color: var(--logo-blue); letter-spacing: 1px; line-height: 1;
  }
  .front-logo-band .brand-name { position: absolute; left: 18px; top: 6px; font-size: 84px; }
  .front-location {
    position: absolute; left: 20px; top: 168px;
    font-family: "Tinos", "Times New Roman", serif; font-weight: 700;
    font-size: 34px; color: var(--cream);
  }
  .front-tagline {
    position: absolute; right: 25px; top: 345px;
    font-family: "Tinos", "Times New Roman", serif; font-weight: 700;
    font-size: 58px; color: var(--yellow); letter-spacing: 0.5px;
  }

  .card-back {
    position: absolute; left: 0; top: 745px; width: 759px; height: 455px;
    background: linear-gradient(90deg, var(--peach) 0%, var(--pale-yellow) 100%);
  }
  .back-brand { position: absolute; right: 50px; top: 22px; text-align: right; }
  .back-brand .brand-name { font-size: 54px; display: block; }
  .back-location {
    display: block; margin-top: 4px;
    font-family: "Tinos", "Times New Roman", serif; font-weight: 700;
    font-size: 19px; color: var(--ink);
  }
  .contact-fields { position: absolute; left: 25px; top: 132px; list-style: none; }
  .contact-field {
    display: flex; align-items: flex-end; height: 46px;
    font-family: "Arimo", Arial, sans-serif; font-size: 30px; color: var(--ink);
  }
  .field-label { white-space: pre; }
  .field-line { border-bottom: 2px solid var(--ink); margin-left: 6px; margin-bottom: 4px; }
  .contact-field.extra-line .field-line { margin-left: 0; }
</style>
</head>
<body>
<div class="canvas">
  <section class="card-front">
    <div class="front-logo-band"><span class="brand-name">wheelnest</span></div>
    <p class="front-location">Melbourne, Australia</p>
    <p class="front-tagline">CAR FOR RENT</p>
  </section>

  <section class="card-back">
    <div class="back-brand">
      <span class="brand-name">wheelnest</span>
      <span class="back-location">Melbourne, Australia</span>
    </div>
    <ul class="contact-fields">
      <li class="contact-field"><span class="field-label">Name :</span><span class="field-line" style="width:512px"></span></li>
      <li class="contact-field"><span class="field-label">Title    :</span><span class="field-line" style="width:490px"></span></li>
      <li class="contact-field"><span class="field-label">Mobile number :</span><span class="field-line" style="width:356px"></span></li>
      <li class="contact-field"><span class="field-label">E-mail :</span><span class="field-line" style="width:490px"></span></li>
      <li class="contact-field"><span class="field-label">Company website :</span><span class="field-line" style="width:262px"></span></li>
      <li class="contact-field extra-line"><span class="field-line" style="width:412px"></span></li>
    </ul>
  </section>
</div>
</body>
</html>
```